KTM Structural Approval Standards Private Assessors

Professional Construction Consultancy Company Business Card - must keep logo colours see images below - examples have been added from my last competition - please see them as examples only!

Target Market(s)

Home Builders

Industry/Entity Type

Construction

Contact Information for Business Card

See "must haves"

Font styles to use
Sans Serif

Colors
ffffff
add136
000000

Requirements
Must have
• Daniel Moravi
• Director
• Phone: 0431 587 219
• Address: 7 Tarrunga Rd,
• Hallworth Vale, SA, 5091
• Email: ktmassessors@mailbox-example.com
• Website: www.ktmassessors-example.com.au
• Facebook: KTM Structural Approval Standards
Nice to have
• Side 1: full logo
• Side 2: company details
Should not have
• hard to read
• must be clear and professional

```html
<!DOCTYPE html>
<html lang="en">
<head>
<meta charset="utf-8">
<title>Structural Approval Standards – Business Card</title>
<link href="https://fonts.googleapis.com/css2?family=Montserrat:wght@500;600&family=Open+Sans:wght@400;600&display=swap" rel="stylesheet">
<style>
  :root {
    --brand-green: #add136;
    --card-black: #000000;
    --card-white: #ffffff;
    --ink: #1a1a1a;
    --muted-grey: #3a3f42;
    --stage: #5e7278;
  }
  * { margin: 0; padding: 0; box-sizing: border-box; }
  html, body { width: 1200px; height: 960px; overflow: hidden; }
  body {
    background: var(--stage);
    font-family: "Open Sans", Arial, sans-serif;
    position: relative;
  }
  .card {
    position: absolute;
    left: 220px;
    width: 760px;
    height: 434px;
    border-radius: 24px;
    overflow: hidden;
  }
  /* Side 1 */
  .card-front { top: 30px; background: var(--card-black); }
  .front-mark {
    position: absolute;
    left: 64px; top: 52px;
    width: 76px; height: 76px;
    background: var(--muted-grey);
  }
  .front-wordmark {
    position: absolute;
    left: 270px; top: 150px;
    width: 420px;
    font-family: "Montserrat", Arial, sans-serif;
    font-weight: 600;
    font-size: 30px;
    line-height: 1.25;
    color: var(--brand-green);
  }
  /* Side 2 */
  .card-back { top: 496px; background: var(--card-white); }
  .accent-bar {
    position: absolute;
    left: 0; top: 52px;
    width: 16px; height: 62px;
    background: var(--brand-green);
  }
  .person {
    position: absolute;
    left: 48px; top: 60px;
    font-family: "Montserrat", Arial, sans-serif;
  }
  .person-name { font-size: 22px; font-weight: 500; color: var(--ink); }
  .person-role { font-size: 17px; font-weight: 500; color: var(--brand-green); margin-top: -2px; }
  .contact-list {
    position: absolute;
    left: 48px; top: 142px;
    list-style: none;
    font-size: 16px;
    color: var(--ink);
  }
  .contact-item {
    display: flex;
    align-items: flex-start;
    gap: 14px;
    margin-bottom: 10px;
    line-height: 1.35;
  }
  .contact-icon { width: 18px; height: 18px; flex: none; margin-top: 2px; fill: var(--brand-green); }
  .back-mark {
    position: absolute;
    right: 64px; top: 46px;
    width: 56px; height: 56px;
    background: var(--muted-grey);
  }
  .back-wordmark {
    position: absolute;
    right: 36px; bottom: 30px;
    width: 250px;
    text-align: right;
    font-family: "Montserrat", Arial, sans-serif;
    font-weight: 600;
    font-size: 15px;
    line-height: 1.25;
    color: var(--brand-green);
  }
</style>
</head>
<body>
  <section class="card card-front" aria-label="Business card side 1">
    <div class="front-mark" aria-hidden="true"></div>
    <div class="front-wordmark">KTM Structural Approval Standards Private Assessors</div>
  </section>

  <section class="card card-back" aria-label="Business card side 2">
    <div class="accent-bar"></div>
    <div class="person">
      <p class="person-name">Daniel Moravi</p>
      <p class="person-role">Director</p>
    </div>
    <ul class="contact-list">
      <li class="contact-item">
        <svg class="contact-icon" viewBox="0 0 24 24"><path d="M6.6 10.8a15 15 0 0 0 6.6 6.6l2.2-2.2a1 1 0 0 1 1-.25 11.4 11.4 0 0 0 3.6.57 1 1 0 0 1 1 1V20a1 1 0 0 1-1 1A17 17 0 0 1 3 4a1 1 0 0 1 1-1h3.5a1 1 0 0 1 1 1c0 1.25.2 2.45.57 3.57a1 1 0 0 1-.25 1z"/></svg>
        <span>0431 587 219</span>
      </li>
      <li class="contact-item">
        <svg class="contact-icon" viewBox="0 0 24 24"><path d="M12 2a7 7 0 0 0-7 7c0 5.25 7 13 7 13s7-7.75 7-13a7 7 0 0 0-7-7zm0 9.5A2.5 2.5 0 1 1 12 6.5a2.5 2.5 0 0 1 0 5z"/></svg>
        <span>7 Tarrunga Rd,<br>Hallworth Vale, SA, 5091</span>
      </li>
      <li class="contact-item">
        <svg class="contact-icon" viewBox="0 0 24 24"><path d="M2 5h20v14H2z M3.5 6.5 12 13l8.5-6.5" stroke="#fff" stroke-width="1.5"/></svg>
        <span>ktmassessors@mailbox-example.com</span>
      </li>
      <li class="contact-item">
        <svg class="contact-icon" viewBox="0 0 24 24"><circle cx="12" cy="12" r="9" fill="none" stroke="#add136" stroke-width="2"/><path d="M3 12h18M12 3c3 3 3 15 0 18M12 3c-3 3-3 15 0 18" fill="none" stroke="#add136" stroke-width="1.5"/></svg>
        <span>www.ktmassessors-example.com.au</span>
      </li>
      <li class="contact-item">
        <svg class="contact-icon" viewBox="0 0 24 24"><rect x="3" y="3" width="18" height="18" rx="2"/></svg>
        <span>KTM Structural Approval Standards</span>
      </li>
    </ul>
    <div class="back-mark" aria-hidden="true"></div>
    <div class="back-wordmark">KTM Structural Approval Standards Private Assessors</div>
  </section>
</body>
</html>
```